Billboard design for agricultural machinery business

hello im looking for roadside advertiement sign to be designed, the sign is 10ft up in the air and is 4ft high and 8ft wide, id image i like a blue background and my logo front and centre and below logo sales - service - parts and then below that the brook meadow symbol and vale symbol, I’d also like the website www.Fernowell.ie on it. i am open to suggestions and designs. blue is #005999 and yellow is rgb (254, 205, 26) ive attached my log and symbols, im open to different colour backgrounds or just white and also open to brook meadow and vale as writhing rather than logos

Target Market(s)

Brook Meadow and vale tractor owners

Industry/Entity Type

Agricultural machine sales service and parts

Colors

Designer to choose colors to be used in the design.

Requirements
Must have
• My logo and colours, brands brook Meadow and vale, website

```html
<!DOCTYPE html>
<html lang="en">
<head>
<meta charset="UTF-8">
<title>Fernowell Billboard</title>
<link rel="stylesheet" href="https://fonts.googleapis.com/css2?family=Montserrat:wght@600;700;800&family=Josefin+Sans:wght@400&display=swap">
<style>
  :root {
    --brand-blue: #005999;
    --field-deep: #0b2f74;
    --field-mid: #1a4a9e;
    --field-light: #2d62b8;
    --brand-yellow: rgb(254, 205, 26);
    --band-white: #f1f1f3;
    --web-blue: #1f6fae;
    --ink-grey: #5a5d63;
    --page-bg: #e9edf2;
    --white: #ffffff;
  }
  * { margin: 0; padding: 0; box-sizing: border-box; }
  html, body {
    width: 1200px;
    height: 900px;
    overflow: hidden;
    background: var(--page-bg);
  }
  .billboard {
    position: absolute;
    left: 40px;
    top: 170px;
    width: 1120px;
    height: 560px;
    overflow: hidden;
    box-shadow: 0 10px 30px rgba(0, 0, 0, 0.15);
  }
  .hero {
    position: absolute;
    inset: 0 0 120px 0;
    background:
      radial-gradient(ellipse at 50% 10%, var(--field-light) 0%, transparent 60%),
      linear-gradient(180deg, var(--field-mid) 0%, var(--field-deep) 100%);
  }
  .brand {
    position: absolute;
    left: 0;
    right: 0;
    top: 160px;
    display: flex;
    justify-content: center;
    align-items: center;
    gap: 22px;
  }
  .brand-dot {
    width: 34px;
    height: 34px;
    border-radius: 50%;
    background: var(--brand-yellow);
  }
  .brand-name {
    font-family: "Montserrat", sans-serif;
    font-weight: 800;
    font-size: 92px;
    letter-spacing: 1px;
    line-height: 1;
    color: var(--white);
  }
  .services {
    position: absolute;
    left: 0;
    right: 0;
    top: 310px;
    text-align: center;
    font-family: "Josefin Sans", sans-serif;
    font-weight: 400;
    font-size: 40px;
    letter-spacing: 1px;
    color: var(--white);
  }
  .partner-band {
    position: absolute;
    left: 0;
    right: 0;
    bottom: 0;
    height: 120px;
    background: var(--band-white);
    display: flex;
    align-items: center;
    padding: 0 44px 0 50px;
  }
  .partner {
    font-family: "Montserrat", sans-serif;
    font-weight: 700;
    font-size: 34px;
    white-space: nowrap;
    color: var(--brand-blue);
  }
  .partner--meadow { margin-right: 64px; }
  .partner--vale { color: var(--ink-grey); margin-right: auto; }
  .website {
    display: flex;
    align-items: center;
    gap: 18px;
  }
  .website-icon { width: 46px; height: 46px; flex: none; }
  .website-address {
    font-family: "Montserrat", sans-serif;
    font-weight: 700;
    font-size: 44px;
    letter-spacing: 0.5px;
    white-space: nowrap;
    color: var(--web-blue);
  }
</style>
</head>
<body>
  <main class="billboard">
    <section class="hero" role="img" aria-label="Photograph of blue-toned crop rows stretching to the horizon across a field">
      <div class="brand">
        <span class="brand-dot"></span>
        <span class="brand-name">Fernowell</span>
      </div>
      <p class="services">SALES - SERVICE - PARTS</p>
    </section>
    <footer class="partner-band">
      <span class="partner partner--meadow">Brook Meadow</span>
      <span class="partner partner--vale">Vale</span>
      <div class="website">
        <svg class="website-icon" viewBox="0 0 48 48" aria-hidden="true">
          <circle cx="24" cy="24" r="24" fill="var(--brand-yellow)"/>
          <g fill="none" stroke="var(--white)" stroke-width="2.2">
            <circle cx="24" cy="24" r="12"/>
            <ellipse cx="24" cy="24" rx="5.5" ry="12"/>
            <line x1="12" y1="24" x2="36" y2="24"/>
          </g>
        </svg>
        <span class="website-address">www.Fernowell.ie</span>
      </div>
    </footer>
  </main>
</body>
</html>
```